Looking for power point temple for video course

Need slides which will be used to create a video course titled

“Wireless Packet Forensics Workshop”

The course will have lots of slide content and also lots of video screen dlow

Iooking for professional grade designs that match my logo and color scheme: Red Grey & white

Other colors shades are welcome so log as they do not clash with the primary colors.

Like Vectors!

Target Market(s)

Information Security & IT

Industry/Entity Type

Security

Requirements
Must have
• Six separate power point slides;
• 1 Cover slide
• 1 table of contents slide
• 2 heading slides 1 light 1 dark
• 2 content aides 1 light 1 dark
• Match the color and theme of my logo
• Look professional
Nice to have
• Custom bullets, icons, charts tables. All should flow with a uniform theme thought the slide template
Should not have
• Not too many stock photos. It’s fine to have a few faded background type images but I want the focus to be on content and on Vectors

```html
<!DOCTYPE html>
<html lang="en">
<head>
<meta charset="utf-8">
<title>Wireless Packet Forensics Workshop – Slide Template</title>
<link href="https://fonts.googleapis.com/css2?family=Montserrat:wght@400;500;600;700&display=swap" rel="stylesheet">
<style>
  :root {
    --slate: #3c4450;
    --slate-deep: #323943;
    --slate-row: #464e5a;
    --slate-label: #555d69;
    --red: #e31e24;
    --grey: #a7a9ad;
    --grey-light: #c9ccd1;
    --ink: #3b3f45;
    --muted: #8a8e94;
    --white: #ffffff;
    --page: #ffffff;
  }
  * { box-sizing: border-box; margin: 0; padding: 0; }
  html, body { width: 1200px; height: 697px; overflow: hidden; background: var(--page); }
  body { position: relative; font-family: "Montserrat", Arial, sans-serif; color: var(--ink); }

  .slide {
    position: absolute; width: 394px; height: 220px; overflow: hidden;
    box-shadow: 0 1px 3px rgba(0,0,0,.25);
  }
  .slide--dark { background: var(--slate); color: var(--white); }
  .slide--light { background: var(--white); }
  .col-1 { left: 3px; } .col-2 { left: 403px; } .col-3 { left: 803px; }
  .row-1 { top: 6px; } .row-2 { top: 238px; } .row-3 { top: 470px; }

  .accent { color: var(--red); }

  /* brand name */
  .brand { position: absolute; display: flex; align-items: center; gap: 3px;
    font-weight: 500; letter-spacing: .2px; }
  .brand__mark { display: block; background: var(--red); }
  .brand--header { font-size: 12px; color: var(--white); }
  .brand--header .brand__mark { width: 10px; height: 10px; }
  .brand--footer { left: 18px; top: 200px; font-size: 7px; }
  .brand--footer .brand__mark { width: 7px; height: 7px; }
  .slide--light .brand--footer { color: var(--ink); }
  .slide--dark .brand--footer { color: var(--white); }

  .page-num { position: absolute; left: 365px; top: 200px; width: 10px; height: 10px;
    border-radius: 50%; background: var(--red); color: var(--white);
    font-size: 5px; line-height: 10px; text-align: center; }

  /* cover */
  .cover-title { position: absolute; left: 18px; top: 130px; font-size: 19.5px;
    font-weight: 400; letter-spacing: 1.2px; line-height: 24px; text-transform: uppercase; }

  /* section titles */
  .slide-title { position: absolute; left: 8px; top: 9px; font-size: 13px; font-weight: 600;
    letter-spacing: .3px; text-transform: uppercase; }
  .slide-title--bar { border-left: 3px solid var(--red); padding-left: 5px; left: 0; top: 6px; line-height: 20px; }

  /* agenda */
  .agenda-panel { position: absolute; left: 0; top: 0; width: 135px; height: 220px; background: var(--slate); }
  .agenda-heading { position: absolute; left: 10px; top: 102px; font-size: 15px; font-weight: 600;
    color: var(--red); letter-spacing: .6px; }
  .agenda-body { position: absolute; left: 135px; top: 0; width: 259px; height: 220px; background: var(--white); }
  .agenda-item { position: absolute; left: 32px; display: flex; gap: 14px; }
  .agenda-item__num { position: relative; width: 30px; height: 30px; flex: none; }
  .agenda-item__num svg { position: absolute; inset: 0; }
  .agenda-item__num span { position: absolute; inset: 0; text-align: center; line-height: 30px;
    color: var(--white); font-size: 11px; }
  .agenda-item__title { font-size: 8.5px; color: var(--ink); margin-top: 1px; }
  .agenda-item__time { font-size: 4.5px; color: var(--red); margin-top: 1px; }
  .agenda-item__text { font-size: 4.5px; color: var(--muted); width: 100px; line-height: 5.5px; }

  /* project design */
  .feature { position: absolute; width: 72px; font-size: 4.8px; line-height: 6px; color: var(--muted); }
  .feature__name { font-size: 6.5px; color: var(--ink); font-weight: 500; line-height: 8px; }
  .feature--left { left: 10px; text-align: right; }
  .feature--right { left: 307px; text-align: left; }
  .feature--alert .feature__name { color: var(--red); }
  .design-note { position: absolute; left: 22px; top: 172px; width: 350px; text-align: center;
    font-size: 4.8px; line-height: 6.5px; color: var(--muted); }

  /* chain */
  .chain-label { position: absolute; width: 64px; text-align: center; font-size: 4.3px;
    line-height: 5px; color: var(--muted); }
  .chain-label b { display: block; font-size: 5.3px; color: var(--ink); font-weight: 600; }
  .chain-label--red b { color: var(--red); }

  /* pricing table */
  .plans { position: absolute; left: 21px; top: 48px; width: 351px; border-collapse: collapse;
    table-layout: fixed; font-size: 5.3px; text-align: center; }
  .plans th { height: 20px; font-weight: 500; color: var(--white); text-transform: uppercase; font-size: 5.5px; }
  .plans th.plans__blank { background: transparent; }
  .plans th.plan--grey { background: var(--grey); }
  .plans th.plan--red { background: var(--red); }
  .plans td { height: 17.4px; background: var(--slate-row); color: var(--white); }
  .plans tr:nth-child(even) td { background: var(--slate-deep); }
  .plans td.plans__label { background: var(--slate-label); font-size: 4.8px; }
  .plans tr:nth-child(even) td.plans__label { background: #4f5763; }
  .plans col.plans__label-col { width: 71px; }
  .plan-btn { position: absolute; top: 183px; width: 44px; height: 11px; border: 1px solid var(--white);
    border-radius: 1px; font-size: 5.3px; font-weight: 600; line-height: 9px; text-align: center; color: var(--white); }

  /* thank you */
  .thanks-photo { position: absolute; inset: 0;
    background: linear-gradient(120deg, #c9ccd0 0%, #e9eaeb 45%, #b7bcc2 70%, #6f6a64 100%); }
  .thanks-panel { position: absolute; inset: 0; }
  .thanks-title { position: absolute; left: 24px; top: 78px; font-size: 25px; font-weight: 500; letter-spacing: .5px; }
  .thanks-sub { position: absolute; left: 26px; top: 108px; font-size: 11.5px; letter-spacing: .3px; }
  .contact { position: absolute; left: 22px; display: flex; align-items: flex-start; gap: 6px;
    font-size: 5.3px; line-height: 6.5px; }
  .contact svg { flex: none; }
  .contact b { font-weight: 600; }
</style>
</head>
<body>

<!-- 1 Cover, logo right -->
<section class="slide slide--dark col-1 row-1">
  <div class="brand brand--header" style="left:250px; top:28px;"><i class="brand__mark"></i>PACKETLAB</div>
  <h1 class="cover-title">Wireless <span class="accent">Packet<br>Forensics</span> Workshop</h1>
</section>

<!-- 2 Cover, logo left -->
<section class="slide slide--dark col-2 row-1">
  <div class="brand brand--header" style="left:20px; top:31px;"><i class="brand__mark"></i>PACKETLAB</div>
  <h1 class="cover-title">Wireless <span class="accent">Packet<br>Forensics</span> Workshop</h1>
</section>

<!-- 3 Agenda -->
<section class="slide slide--light col-3 row-1">
  <div class="agenda-panel"></div>
  <h2 class="agenda-heading">OUR AGENDA</h2>
  <div class="agenda-body">
    <div class="agenda-item" style="top:28px;">
      <div class="agenda-item__num"><svg viewBox="0 0 30 30"><polygon points="15,2 28,15 15,28 2,15" fill="#3c4450"/><polyline points="3,18 15,30 27,18" fill="none" stroke="#e31e24" stroke-width=".8"/></svg><span>1</span></div>
      <div><p class="agenda-item__title">Agenda One</p><p class="agenda-item__time">10:00</p><p class="agenda-item__text">Brief summary of what this part of the course covers.</p></div>
    </div>
    <div class="agenda-item" style="top:71px;">
      <div class="agenda-item__num"><svg viewBox="0 0 30 30"><polygon points="15,2 28,15 15,28 2,15" fill="#3c4450"/><polyline points="3,18 15,30 27,18" fill="none" stroke="#e31e24" stroke-width=".8"/></svg><span>2</span></div>
      <div><p class="agenda-item__title">Agenda Two</p><p class="agenda-item__time">11:00</p><p class="agenda-item__text">Brief summary of what this part of the course covers.</p></div>
    </div>
    <div class="agenda-item" style="top:114px;">
      <div class="agenda-item__num"><svg viewBox="0 0 30 30"><polygon points="15,2 28,15 15,28 2,15" fill="#3c4450"/><polyline points="3,18 15,30 27,18" fill="none" stroke="#e31e24" stroke-width=".8"/></svg><span>3</span></div>
      <div><p class="agenda-item__title">Agenda Three</p><p class="agenda-item__time">12:00</p><p class="agenda-item__text">Brief summary of what this part of the course covers.</p></div>
    </div>
    <div class="agenda-item" style="top:157px;">
      <div class="agenda-item__num"><svg viewBox="0 0 30 30"><polygon points="15,2 28,15 15,28 2,15" fill="#3c4450"/><polyline points="3,18 15,30 27,18" fill="none" stroke="#e31e24" stroke-width=".8"/></svg><span>4</span></div>
      <div><p class="agenda-item__title">Agenda Four</p><p class="agenda-item__time">13:00</p><p class="agenda-item__text">Brief summary of what this part of the course covers.</p></div>
    </div>
  </div>
</section>

<!-- 4 Project design -->
<section class="slide slide--light col-1 row-2">
  <h2 class="slide-title slide-title--bar">Project <span class="accent">Design</span></h2>
  <svg class="layer-stack" style="position:absolute; left:130px; top:44px;" width="132" height="120" viewBox="0 0 132 120" aria-hidden="true">
    <g>
      <polygon points="20,104 112,104 126,112 6,112" fill="#7a7f86"/>
      <polygon points="20,92 112,92 126,101 6,101" fill="#5d636b"/>
      <polygon points="20,80 112,80 126,89 6,89" fill="#b9bcc0"/>
      <polygon points="20,68 112,68 126,77 6,77" fill="#d5d7da"/>
      <polygon points="20,56 112,56 126,65 6,65" fill="#e31e24"/>
      <polygon points="20,44 112,44 126,53 6,53" fill="#c9ccd0"/>
      <polygon points="20,32 112,32 126,41 6,41" fill="#6d737b"/>
      <polygon points="20,20 112,20 126,29 6,29" fill="#e8777a"/>
      <polygon points="20,10 112,10 126,18 6,18" fill="#e34a4e"/>
      <polygon points="28,2 104,2 116,9 16,9" fill="#d9dbde"/>
    </g>
  </svg>
  <svg style="position:absolute; left:88px; top:67px;" width="26" height="26" viewBox="0 0 26 26" aria-hidden="true"><circle cx="13" cy="13" r="13" fill="#3c4450"/><rect x="7" y="8" width="12" height="8" fill="none" stroke="#fff" stroke-width="1.3"/><line x1="13" y1="16" x2="13" y2="19" stroke="#fff" stroke-width="1.3"/><line x1="10" y1="19" x2="16" y2="19" stroke="#fff" stroke-width="1.3"/></svg>
  <svg style="position:absolute; left:88px; top:114px;" width="26" height="26" viewBox="0 0 26 26" aria-hidden="true"><circle cx="13" cy="13" r="13" fill="#e31e24"/><path d="M8 15a3 3 0 0 1 1-6 4 4 0 0 1 8 0 3 3 0 0 1 1 6z" fill="#fff"/><path d="M13 11v5m-2-2 2 2 2-2" stroke="#e31e24" stroke-width="1.1" fill="none"/></svg>
  <svg style="position:absolute; left:275px; top:67px;" width="26" height="26" viewBox="0 0 26 26" aria-hidden="true"><circle cx="13" cy="13" r="13" fill="#e31e24"/><ellipse cx="13" cy="12" rx="6" ry="4.5" fill="#fff"/><polygon points="9,15 8,19 12,16" fill="#fff"/></svg>
  <svg style="position:absolute; left:275px; top:114px;" width="26" height="26" viewBox="0 0 26 26" aria-hidden="true"><circle cx="13" cy="13" r="13" fill="#3c4450"/><polygon points="13,6 17,18 9,18" fill="#fff"/><rect x="7" y="18" width="12" height="2" fill="#fff"/><rect x="10" y="12" width="6" height="1.4" fill="#3c4450"/></svg>
  <div class="feature feature--left" style="top:68px;"><p class="feature__name">Digital</p>Short note on this step in the capture workflow.</div>
  <div class="feature feature--left feature--alert" style="top:115px;"><p class="feature__name">Warning</p>Short note on this step in the capture workflow.</div>
  <div class="feature feature--right feature--alert" style="top:68px;"><p class="feature__name">Teamwork</p>Short note on this step in the capture workflow.</div>
  <div class="feature feature--right" style="top:115px;"><p class="feature__name">Rotation</p>Short note on this step in the capture workflow.</div>
  <p class="design-note">Use this space for a short summary of the project plan, the tools you will use and the main goals of each module in this workshop. Keep it to two lines so the slide stays clean and easy to read.</p>
  <div class="brand brand--footer"><i class="brand__mark"></i>PACKETLAB</div>
  <div class="page-num">5</div>
</section>

<!-- 5 Chain process -->
<section class="slide slide--light col-2 row-2">
  <h2 class="slide-title slide-title--bar">Chainlink <span class="accent">Process</span></h2>
  <svg style="position:absolute; left:0; top:0;" width="394" height="220" viewBox="0 0 394 220" aria-hidden="true">
    <g stroke-width="14" stroke-linecap="round">
      <line x1="66" y1="127" x2="100" y2="93" stroke="#3c4450"/>
      <line x1="100" y1="93" x2="133" y2="127" stroke="#e31e24"/>
      <line x1="133" y1="127" x2="168" y2="93" stroke="#a7a9ad"/>
      <line x1="168" y1="93" x2="202" y2="127" stroke="#3c4450"/>
      <line x1="202" y1="127" x2="236" y2="93" stroke="#e31e24"/>
      <line x1="236" y1="93" x2="269" y2="127" stroke="#3c4450"/>
      <line x1="269" y1="127" x2="303" y2="93" stroke="#b4bccb"/>
      <line x1="303" y1="93" x2="338" y2="127" stroke="#c9ccd1"/>
    </g>
    <g stroke="#fff" stroke-width="1.4">
      <circle cx="66" cy="127" r="18" fill="#3c4450"/>
      <circle cx="100" cy="93" r="18" fill="#e31e24"/>
      <circle cx="133" cy="127" r="18" fill="#a7a9ad"/>
      <circle cx="168" cy="93" r="18" fill="#3c4450"/>
      <circle cx="202" cy="127" r="18" fill="#e31e24"/>
      <circle cx="236" cy="93" r="18" fill="#3c4450"/>
      <circle cx="269" cy="127" r="18" fill="#b4bccb"/>
      <circle cx="303" cy="93" r="18" fill="#c9ccd1"/>
      <circle cx="338" cy="127" r="18" fill="#c9ccd1"/>
    </g>
    <g fill="#fff">
      <circle cx="66" cy="127" r="12"/><circle cx="100" cy="93" r="12" fill="#e31e24" stroke="#fff"/>
      <circle cx="133" cy="127" r="12" fill="#a7a9ad" stroke="#fff"/><circle cx="168" cy="93" r="12"/>
      <circle cx="202" cy="127" r="12" fill="#e31e24" stroke="#fff"/><circle cx="236" cy="93" r="12"/>
      <circle cx="269" cy="127" r="12" fill="#b4bccb" stroke="#fff"/><circle cx="303" cy="93" r="12"/>
      <circle cx="338" cy="127" r="12" fill="#c9ccd1" stroke="#fff"/>
    </g>
    <g fill="none" stroke-width="1.2" stroke-linecap="round" stroke-linejoin="round">
      <path d="M62 122h6l3 3v7h-9z" stroke="#3c4450"/>
      <path d="M95 96a3 3 0 0 1 1-6 4 4 0 0 1 8 0 3 3 0 0 1 1 6zM100 95v-4m-2 2 2-2 2 2" stroke="#fff"/>
      <path d="M128 123h10v5h-10zM130 128v4m6-4v4" stroke="#fff"/>
      <path d="M163 96a3 3 0 0 1 1-6 4 4 0 0 1 8 0 3 3 0 0 1 1 6zM168 91v4m-2-2 2 2 2-2" stroke="#3c4450"/>
      <path d="M197 124a5 5 0 0 1 9-1m1 7a5 5 0 0 1-9 1M206 121v2h-2m-6 8v-2h2" stroke="#fff"/>
      <path d="M231 88l10 10m0-10-10 10" stroke="#3c4450"/>
      <path d="M266 130a4 4 0 1 1 6 0v2h-6zM267 134h4" stroke="#fff"/>
      <path d="M298 87h10v12h-10zM300 93l2 2 4-4" stroke="#a7a9ad"/>
      <path d="M333 131a5 5 0 1 1 10 0M338 127l2-2" stroke="#fff"/>
    </g>
  </svg>
  <div class="chain-label chain-label--red" style="left:68px; top:52px;"><b>Description</b>Short text on this stage of packet review.</div>
  <div class="chain-label" style="left:136px; top:52px;"><b>Description</b>Short text on this stage of packet review.</div>
  <div class="chain-label" style="left:204px; top:52px;"><b>Description</b>Short text on this stage of packet review.</div>
  <div class="chain-label" style="left:271px; top:52px;"><b>Description</b>Short text on this stage of packet review.</div>
  <div class="chain-label" style="left:34px; top:150px;"><b>Description</b>Short text on this stage of packet review.</div>
  <div class="chain-label" style="left:101px; top:150px;"><b>Description</b>Short text on this stage of packet review.</div>
  <div class="chain-label chain-label--red" style="left:170px; top:150px;"><b>Description</b>Short text on this stage of packet review.</div>
  <div class="chain-label" style="left:237px; top:150px;"><b>Description</b>Short text on this stage of packet review.</div>
  <div class="chain-label" style="left:306px; top:150px;"><b>Description</b>Short text on this stage of packet review.</div>
  <div class="brand brand--footer"><i class="brand__mark"></i>PACKETLAB</div>
  <div class="page-num">6</div>
</section>

<!-- 6 Simple table -->
<section class="slide slide--dark col-3 row-2">
  <h2 class="slide-title">Simple <span class="accent">Table</span></h2>
  <table class="plans">
    <colgroup><col class="plans__label-col"><col><col><col><col></colgroup>
    <tr><th class="plans__blank"></th><th class="plan--grey">Basic</th><th class="plan--red">Student</th><th class="plan--grey">Business</th><th class="plan--red">Corporate</th></tr>
    <tr><td class="plans__label">Users</td><td>1</td><td>5</td><td>15</td><td>50</td></tr>
    <tr><td class="plans__label">Domain Name</td><td>1</td><td>3</td><td>5</td><td>10</td></tr>
    <tr><td class="plans__label">Storage</td><td>1 GB</td><td>5 GB</td><td>10 GB</td><td>unlimited</td></tr>
    <tr><td class="plans__label">Uploads</td><td>10 GB</td><td>50 GB</td><td>250 GB</td><td>unlimited</td></tr>
    <tr><td class="plans__label">Support</td>
      <td><svg width="9" height="9" viewBox="0 0 10 10" aria-label="No"><circle cx="5" cy="5" r="5" fill="#e31e24"/><path d="M3 3l4 4M7 3l-4 4" stroke="#fff" stroke-width="1.2"/></svg></td>
      <td><svg width="9" height="9" viewBox="0 0 10 10" aria-label="Yes"><circle cx="5" cy="5" r="5" fill="#c9ccd1"/><path d="M2.8 5.2l1.6 1.6 3-3.2" stroke="#3c4450" stroke-width="1.2" fill="none"/></svg></td>
      <td><svg width="9" height="9" viewBox="0 0 10 10" aria-label="Yes"><circle cx="5" cy="5" r="5" fill="#c9ccd1"/><path d="M2.8 5.2l1.6 1.6 3-3.2" stroke="#3c4450" stroke-width="1.2" fill="none"/></svg></td>
      <td><svg width="9" height="9" viewBox="0 0 10 10" aria-label="Yes"><circle cx="5" cy="5" r="5" fill="#c9ccd1"/><path d="M2.8 5.2l1.6 1.6 3-3.2" stroke="#3c4450" stroke-width="1.2" fill="none"/></svg></td></tr>
    <tr><td class="plans__label">Offer</td><td>---</td><td>---</td><td>one month free</td><td>three month free</td></tr>
  </table>
  <div class="plan-btn" style="left:105px;">Get this Plan</div>
  <div class="plan-btn" style="left:175px;">Get this Plan</div>
  <div class="plan-btn" style="left:245px;">Get this Plan</div>
  <div class="plan-btn" style="left:315px;">Get this Plan</div>
  <div class="brand brand--footer"><i class="brand__mark"></i>PACKETLAB</div>
  <div class="page-num">7</div>
</section>

<!-- 7 Light content -->
<section class="slide slide--light col-1 row-3">
  <h2 class="slide-title slide-title--bar">Your Light <span class="accent">Content Slide</span></h2>
  <div class="brand brand--footer"><i class="brand__mark"></i>PACKETLAB</div>
  <div class="page-num">8</div>
</section>

<!-- 8 Dark content -->
<section class="slide slide--dark col-2 row-3">
  <h2 class="slide-title">Your Dark <span class="accent">Content Slide</span></h2>
  <div class="brand brand--footer"><i class="brand__mark"></i>PACKETLAB</div>
  <div class="page-num">9</div>
</section>

<!-- 9 Thank you -->
<section class="slide slide--dark col-3 row-3">
  <div class="thanks-photo" role="img" aria-label="Faded photo of hands using a tablet beside a coffee cup on a desk"></div>
  <svg class="thanks-panel" width="394" height="220" viewBox="0 0 394 220" aria-hidden="true"><polygon points="0,0 252,0 162,220 0,220" fill="#3c4450" fill-opacity=".95"/></svg>
  <div class="brand brand--header" style="left:22px; top:24px;"><i class="brand__mark"></i>PACKETLAB</div>
  <h2 class="thanks-title">Thank <span class="accent">You</span></h2>
  <p class="thanks-sub">Send Your Feedback</p>
  <div class="contact" style="top:136px;"><svg width="8" height="8" viewBox="0 0 10 10"><path d="M1 5l4-4 4 4H8v4H2V5z" fill="#fff"/></svg><div><b>48 Harbor Lane</b><br>Portview 20417</div></div>
  <div class="contact" style="top:154px;"><svg width="8" height="8" viewBox="0 0 10 10"><path d="M2 1l2 2-1 1.5a6 6 0 0 0 2.5 2.5L7 6l2 2-1.5 1.5C4 9 1 6 .5 2.5z" fill="#fff"/></svg><div>(555) 019-2834</div></div>
  <div class="contact" style="top:166px;"><svg width="8" height="8" viewBox="0 0 10 10"><rect x="1" y="2" width="8" height="6" fill="#fff"/><path d="M1 2l4 3.5L9 2" stroke="#3c4450" fill="none" stroke-width=".8"/></svg><div><b>hello@packetlab.io</b></div></div>
  <div class="contact" style="top:180px;"><svg width="8" height="8" viewBox="0 0 10 10"><circle cx="5" cy="5" r="4.2" fill="none" stroke="#fff" stroke-width="1.2"/><path d="M1 5h8M5 1c-2 2.5-2 5.5 0 8M5 1c2 2.5 2 5.5 0 8" stroke="#fff" fill="none" stroke-width=".7"/></svg><div><b>www.packetlab.io</b></div></div>
</section>

</body>
</html>
```